Wine Bottle Lable

Want a unique, simple but elegant, label for a wine bottle. I want to use the letters "DKP" in the design which is a moniker for my last name "Dufkamp". The letters DKP do not have to be juxtaposed together so that it is recognizable, or they could be something like D-KP, KP-D, DPK D-KP-D, etc. The X could be totally separated from the NO, or otherwise. The wine is a white wine in a clear bottle. I need Adobe Illustrator files so I can add the wine varietal, year, alcohol content. The label should be 4" wide and 5" tall.

Colors

Designer to choose colors to be used in the design.

Requirements
Nice to have
• outstanding but simple graphics

```html
<!DOCTYPE html>
<html lang="en">
<head>
<meta charset="utf-8">
<title>DKP Sauvignon Blanc — Label</title>
<link href="https://fonts.googleapis.com/css2?family=Bodoni+Moda:opsz,wght@6..96,500&family=Mr+Dafoe&family=Poppins:wght@400&display=swap" rel="stylesheet">
<style>
  :root {
    --page: #f2f1f0;
    --paper: #e9e3e3;
    --ink: #2b2119;
    --night: #0b0b0b;
    --silver: #8d8d8d;
    --wine-red: #c4161c;
    --gold: #a88a3c;
    --small-light: #2a2a2a;
    --small-dark: #f2f2f2;
    --roo-light: #2b2119;
    --roo-dark: #2a2a2a;
  }
  * { box-sizing: border-box; margin: 0; padding: 0; }
  html, body {
    width: 1200px; height: 1200px; overflow: hidden;
    background: var(--page);
  }
  .sheet {
    width: 1200px; height: 1200px;
    display: flex; align-items: center; justify-content: center; gap: 80px;
  }
  .label {
    position: relative;
    width: 440px; height: 550px;
    overflow: hidden;
    box-shadow: 0 10px 30px rgba(0,0,0,0.12);
  }
  .label--light { background: var(--paper); --mark: var(--ink); --small: var(--small-light); --roo: var(--roo-light); }
  .label--dark  { background: var(--night); --mark: var(--silver); --small: var(--small-dark); --roo: var(--roo-dark); }

  .monogram {
    font-family: "Bodoni Moda", "Didot", serif;
    font-weight: 500;
    color: var(--mark);
    position: absolute;
    line-height: 1;
    white-space: nowrap;
  }
  .monogram__d {
    font-size: 420px;
    left: -18px; top: 9px;
  }
  .monogram__kp {
    font-size: 110px;
    left: 284px; top: 205px;
    letter-spacing: 0.01em;
  }
  .varietal {
    position: absolute; left: 0; right: 0; top: 398px;
    text-align: center;
    font-family: "Mr Dafoe", cursive;
    font-size: 56px;
    color: var(--wine-red);
    line-height: 1;
  }
  .vintage {
    position: absolute; left: 0; right: 0; top: 470px;
    text-align: center;
    font-family: "Bodoni Moda", serif;
    font-size: 17px;
    color: var(--gold);
    text-decoration: underline;
    text-underline-offset: 3px;
    text-decoration-thickness: 1px;
  }
  .volume {
    position: absolute; left: 0; right: 0; top: 506px;
    text-align: center;
    font-family: "Poppins", sans-serif;
    font-size: 11.5px;
    color: var(--small);
    letter-spacing: 0.02em;
  }
  .kangaroo {
    position: absolute; right: 8px; bottom: 0;
    width: 96px; height: 80px;
    background: var(--roo);
    opacity: 0.9;
    border-radius: 40px 30px 0 0;
  }
</style>
</head>
<body>
<main class="sheet">
  <article class="label label--light">
    <span class="monogram monogram__d">D</span>
    <span class="monogram monogram__kp">KP</span>
    <p class="varietal">Sauvignon Blanc</p>
    <p class="vintage">2019</p>
    <p class="volume">750ML 13.5% ALC/VOL</p>
    <div class="kangaroo" role="img" aria-label="Kangaroo silhouette"></div>
  </article>

  <article class="label label--dark">
    <span class="monogram monogram__d">D</span>
    <span class="monogram monogram__kp">KP</span>
    <p class="varietal">Sauvignon Blanc</p>
    <p class="vintage">2019</p>
    <p class="volume">750ML 13.5% ALC/VOL</p>
    <div class="kangaroo" role="img" aria-label="Kangaroo silhouette"></div>
  </article>
</main>
</body>
</html>
```